Flyer für ambulante und teilstationäre Pflege
Zielgruppe
ambulante und teilstationäre Pflege
Zielgruppe: Pflegebedürftige Menschen, die noch ausreichend mobil sind, um als Gast in unserer Tagespflege zu sein
Aufgabenstellung
Standard DIN lang Format
Stil soll unserer Homepage folgen: www.betreuung-sonnwik.de
Wir achten immer sehr darauf, nicht so einen verstaubten Stil wie viele andere Pflegeeinrichtungen zu haben, sondern fröhlich, bunt , ansprechend

```html
<!DOCTYPE html>
<html lang="de">
<head>
<meta charset="utf-8">
<title>Flyer DIN lang – Pflege Sonnwik</title>
<link href="https://fonts.googleapis.com/css2?family=PT+Sans+Narrow:wght@400;700&family=Tinos&display=swap" rel="stylesheet">
<style>
:root{
  --teal:#1a9aa0;
  --teal-light:#bfe1e1;
  --paper:#e9f4f4;
  --red:#b0262a;
  --ink:#2c2c2c;
  --grey:#6a6a6a;
  --stage:#e6e6e6;
}
*{box-sizing:border-box;margin:0;padding:0}
html,body{width:1200px;height:1200px;overflow:hidden;background:var(--stage)}
body{position:relative;font-family:"PT Sans Narrow",sans-serif;color:var(--ink)}
.spread{position:absolute;left:193px;width:813px;height:575px;
  background:linear-gradient(180deg,#f4fafa 0%,var(--paper) 45%,var(--teal-light) 100%);overflow:hidden;
  box-shadow:0 2px 6px rgba(0,0,0,.15)}
.spread--outside{top:10px}
.spread--inside{top:612px}
.spread__art{position:absolute;inset:0}
.fold{position:absolute;top:0;bottom:0;width:1px;background:rgba(0,0,0,.12)}
.panel{position:absolute;top:0;height:575px;width:271px}
.panel--1{left:0}.panel--2{left:271px}.panel--3{left:542px}
.heading{position:absolute;font-family:"Tinos",serif;font-weight:400;color:var(--red);font-size:14px;white-space:nowrap}
.body-text{position:absolute;font-size:9.2px;line-height:1.38}
.body-text p{margin-bottom:7px}
.list{list-style:none}
.list li{position:relative;padding-left:9px;margin-bottom:6px}
.list li::before{content:"•";position:absolute;left:0;color:var(--grey)}
.photo{position:absolute;background:linear-gradient(135deg,#8fa6b0,#c8a58a 55%,#5d7e86)}
.photo--round{border-radius:50%}
.badge{position:absolute;border-radius:50%;background:var(--teal);color:#fff;font-weight:700;
  text-align:center;display:flex;align-items:center;justify-content:center;font-size:8px;line-height:1.25;padding:10px}
.brand{position:absolute;color:var(--grey);letter-spacing:.5px;white-space:nowrap}
.brand__name{font-size:12px;text-transform:uppercase}
.brand__sub{font-size:6.5px;text-transform:uppercase;text-align:right}
.brand__dot{position:absolute;border-radius:50%}
.brand__dot--red{background:var(--red)}
.brand__dot--teal{background:var(--teal)}
.address{position:absolute;font-size:9px;line-height:1.35}
.address b{font-weight:700}
.address i{font-style:italic}
.address p{margin-bottom:8px}
.title{position:absolute;left:8px;width:255px;top:46px;text-align:center;font-family:"Tinos",serif;font-weight:400;
  color:var(--teal);font-size:28px;line-height:1.22;white-space:nowrap}
</style>
</head>
<body>

<section class="spread spread--outside">
  <svg class="spread__art" viewBox="0 0 813 575" aria-hidden="true">
    <defs>
      <linearGradient id="tealWave" x1="0" x2="1">
        <stop offset="0" stop-color="#8cc8ca"/><stop offset=".6" stop-color="#1a9aa0"/><stop offset="1" stop-color="#5fb6b8"/>
      </linearGradient>
      <linearGradient id="rustWave" x1="0" x2="1">
        <stop offset="0" stop-color="#b5452e"/><stop offset="1" stop-color="#d9a28a"/>
      </linearGradient>
      <linearGradient id="bottomWave" x1="0" x2="1">
        <stop offset="0" stop-color="#1a9aa0"/><stop offset=".5" stop-color="#8fcbcc"/><stop offset="1" stop-color="#1a9aa0"/>
      </linearGradient>
    </defs>
    <path d="M0 0 H560 C520 40 440 80 310 92 C190 104 90 80 0 40 Z" fill="url(#tealWave)"/>
    <path d="M0 0 H300 C220 30 120 40 0 22 Z" fill="#c9e6e6" opacity=".7"/>
    <path d="M520 0 H813 V28 C740 18 660 22 545 40 C560 20 545 8 520 0 Z" fill="url(#rustWave)"/>
    <path d="M0 575 V545 C130 520 260 560 420 540 C560 522 700 530 813 548 V575 Z" fill="url(#bottomWave)" opacity=".85"/>
  </svg>
  <div class="fold" style="left:271px"></div>
  <div class="fold" style="left:542px"></div>

  <div class="panel panel--1">
    <h2 class="heading" style="left:42px;top:108px">Stärken unserer Einrichtung:</h2>
    <ul class="body-text list" style="left:40px;top:150px;width:205px">
      <li>Individuelle und fachlich differenzierte Einschätzung der Pflegebedarfe und Maßnahmenplanung, sehr gute Schmerzeinschätzung</li>
      <li>Förderung der Selbstbestimmtheit der Tagesgäste</li>
      <li>Positiv empfundener familiärer Charakter der Pflegeeinrichtung</li>
      <li>Gute, aussagekräftige Schilderungen in den Pflegeberichten</li>
      <li>Hohe geäußerte Zufriedenheit mit der pflegerischen Versorgung und sozialen Betreuung durch die versorgten Personen</li>
      <li>Individuelle Pflege und Berücksichtigung biographischer Besonderheiten</li>
      <li>Umfangreiches Beschäftigungsprogramm in der Gruppe und einzeln</li>
    </ul>
    <div class="photo photo--round" role="img" aria-label="Foto: Betreuerin musiziert mit Gitarre gemeinsam mit einem Tagesgast" style="left:115px;top:405px;width:175px;height:175px"></div>
    <div class="badge" style="left:30px;top:435px;width:82px;height:82px">Lassen Sie sich von unseren Pflegeexperten zu unserer Pflege beraten. Rufen Sie uns gerne an!</div>
  </div>

  <div class="panel panel--2">
    <h2 class="heading" style="left:33px;top:108px">Unsere beiden Standorte</h2>
    <div class="brand" style="left:33px;top:168px">
      <div class="brand__name">Ambulante Pflege Sonnwik</div>
      <div class="brand__sub">Sonnwik · Nordhafen · Moorbek</div>
      <span class="brand__dot brand__dot--red" style="left:158px;top:-1px;width:24px;height:24px"></span>
    </div>
    <div class="address" style="left:35px;top:212px;width:220px">
      <p><b>Hauptsitz</b><br>Dorfstraße 12<br>24999 Sonnwik<br>Telefon: +49(0)4300 1234</p>
      <p>E-Mail: info@betreuung-sonnwik.de</p>
      <p><b>Sprechzeiten Verwaltung</b><br>Montag bis Freitag 07.30 bis 14.00 Uhr<br><i>Samstag und Sonntag geschlossen</i></p>
    </div>
    <div class="brand" style="left:33px;top:378px">
      <div class="brand__name">Tagespflege am Lindenhof</div>
      <div class="brand__sub">Nordhafen</div>
      <span class="brand__dot brand__dot--teal" style="left:156px;top:-3px;width:24px;height:24px"></span>
    </div>
    <div class="address" style="left:35px;top:420px;width:150px">
      <p>Lindenweg 7<br>24998 Nordhafen<br>Telefon: +49(0)431 00 11 22 33</p>
      <p>E-Mail: info@betreuung-sonnwik.de</p>
      <p><b>Öffnungszeiten Tagespflege</b><br>Montag bis Freitag<br>8.30 bis 16.30 Uhr<br><i>Samstag und Sonntag<br>geschlossen</i></p>
    </div>
    <div class="badge" style="left:148px;top:487px;width:88px;height:88px">Wir bitten um Terminvereinbarung, bevor Sie unsere Einrichtung aufsuchen!</div>
  </div>

  <div class="panel panel--3">
    <h1 class="title">Der Pflegedienst,<br>der die Freude<br>ins Leben zurück<br>bringt</h1>
    <div class="photo" role="img" aria-label="Foto: Gruppe älterer Menschen auf einer Parkbank vor dem Kleinbus des Pflegedienstes" style="left:18px;top:195px;width:238px;height:150px;border-radius:38% 12% 30% 18% / 30% 20% 25% 20%;background:linear-gradient(160deg,#c7d3dc 0%,#8a9a8c 45%,#6f6a55 70%,#a7b48a 100%)"></div>
    <div class="brand" style="left:30px;top:408px">
      <div class="brand__name" style="font-size:15px">Tagespflege am Lindenhof</div>
      <div class="brand__sub" style="font-size:8px">Nordhafen</div>
      <span class="brand__dot brand__dot--teal" style="left:196px;top:-6px;width:30px;height:30px"></span>
    </div>
    <div class="brand" style="left:22px;top:492px">
      <div class="brand__name" style="font-size:15px">Ambulante Pflege Sonnwik</div>
      <div class="brand__sub" style="font-size:8px;text-align:center">Sonnwik · Nordhafen · Moorbek</div>
      <span class="brand__dot brand__dot--red" style="left:204px;top:-6px;width:30px;height:30px"></span>
    </div>
  </div>
</section>

<section class="spread spread--inside">
  <div class="photo" role="img" aria-label="Foto: Brezeln und Senioren beim gemeinsamen Frühstück" style="left:0;top:0;width:271px;height:110px;background:linear-gradient(90deg,#c9a97e,#8e9aa6 50%,#b89c88)"></div>
  <div class="photo" role="img" aria-label="Foto: Tagesgäste spielen gemeinsam ein Brettspiel" style="left:271px;top:0;width:271px;height:110px;background:linear-gradient(90deg,#9c8f88,#7d4b4f 55%,#a59f98)"></div>
  <div class="photo" role="img" aria-label="Foto: Gemeinschaftsraum der Tagespflege mit Blumen und Schild" style="left:542px;top:0;width:271px;height:110px;background:linear-gradient(90deg,#d9dbe0,#b9c7cf 60%,#8a6a96)"></div>
  <svg class="spread__art" viewBox="0 0 813 575" aria-hidden="true">
    <defs>
      <linearGradient id="innerPaper" x1="0" y1="0" x2="0" y2="1">
        <stop offset="0" stop-color="#f4fafa"/><stop offset=".5" stop-color="#e9f4f4"/><stop offset="1" stop-color="#bfe1e1"/>
      </linearGradient>
    </defs>
    <path d="M0 82 C120 100 200 120 320 80 C420 50 520 70 620 62 C700 56 760 50 813 46 V575 H0 Z" fill="url(#innerPaper)"/>
    <path d="M0 86 C120 106 200 126 320 86 C420 56 520 76 620 68 C700 62 760 56 813 52" stroke="#1a9aa0" stroke-width="6" fill="none" opacity=".55"/>
    <path d="M0 575 V548 C150 530 300 560 460 545 C600 532 700 540 813 550 V575 Z" fill="#1a9aa0" opacity=".75"/>
  </svg>
  <div class="fold" style="left:271px"></div>
  <div class="fold" style="left:542px"></div>

  <div class="panel panel--1">
    <h2 class="heading" style="left:42px;top:108px">Ambulante Pflege</h2>
    <div class="body-text" style="left:40px;top:148px;width:210px">
      <p>Die Ambulante Pflege Sonnwik wurde 1994 in Sonnwik gegründet und ist seither stetig gewachsen. Inzwischen umfasst unser Team über 70 qualifizierte Mitarbeiter und wir versorgen und betreuen mehr als 250 Menschen in der Region Sonnwik, Birkenau, Steinort sowie Nordhafen, Moorbek und Umland.</p>
      <p>Einen ambulanten Pflegedienst in Anspruch zu nehmen, bedeutet zunächst fremden Menschen zu vertrauen. Deswegen möchten wir uns bei einem Erstgespräch vorstellen und uns gegenseitig kennenlernen. Hier finden Sie einen ersten Überblick und Informationen über unser Leistungsangebot:</p>
      <ul class="list">
        <li>Individuelle Beratung zu Pflege &amp; Kostenübernahme</li>
        <li>gutes Körpergefühl &amp; frisches Aussehen</li>
        <li>Gesundheit &amp; Vitalität</li>
        <li>Entlastung in Haushalt &amp; Alltag</li>
        <li>Aktivierende Beschäftigung &amp; Demenzbetreuung</li>
        <li>Krankenhausvermeidung</li>
        <li>Verhinderungs- &amp; Urlaubspflege</li>
        <li>Palliativpflege &amp; Sterbebegleitung</li>
        <li>24-Stunden-Notruf</li>
        <li>systemische Beratung &amp; familientherapeutische Begleitung</li>
      </ul>
    </div>
  </div>

  <div class="panel panel--2">
    <h2 class="heading" style="left:45px;top:108px">Tagespflege</h2>
    <div class="body-text" style="left:45px;top:148px;width:205px">
      <p>Seit dem 15.01.2019 besitzen wir eine teilstationäre Tagespflegeeinrichtung mit 16 Plätzen im Gesundheitszentrum Nordhafen. So können wir Ihnen auf einer Fläche von 243 m² mit Sonnenterrasse in gemütlicher Atmosphäre noch mehr Unterstützung anbieten.</p>
      <ul class="list" style="margin-top:26px">
        <li>Abwechslungsreiche Beschäftigung in der Tagespflege</li>
        <li>Individuelle und fachlich differenzierte Einschätzung der Pflegebedarfe und Maßnahmenplanung, sehr gute Schmerzeinschätzung</li>
        <li>Förderung der Selbstbestimmtheit der Tagesgäste</li>
        <li>Positiv empfundener familiärer Charakter der Pflegeeinrichtung</li>
        <li>Gute, aussagekräftige Schilderungen in den Pflegeberichten</li>
        <li>Hohe geäußerte Zufriedenheit mit der pflegerischen Versorgung und sozialen Betreuung durch die versorgten Personen</li>
        <li>Individuelle Pflege und Berücksichtigung biographischer Besonderheiten</li>
        <li>Umfangreiches Beschäftigungsprogramm in der Gruppe und einzeln</li>
      </ul>
    </div>
  </div>

  <div class="panel panel--3">
    <h2 class="heading" style="left:45px;top:108px">Wir sind Pflegeprofis</h2>
    <div class="body-text" style="left:45px;top:148px;width:205px">
      <p>Wir wissen, wie wertvoll gut ausgebildete, erfahrene und motivierte Mitarbeiter sind, um den wachsenden Herausforderungen gerecht zu werden. In vielen Bereichen haben wir Mitarbeiter daher spezialisiert, u.a. in Demenzbetreuung, Palliativpflege, Praxisanleitung, Medizinproduktesicherheit, Datenschutz, Hygiene, Wundmanagement, Insulingabeper Pen, Pflegeberatung, Klangschalentherapie bei Demenz uvm.</p>
    </div>
    <div class="photo photo--round" role="img" aria-label="Foto: Pflegerin liest einer älteren Dame aus einem Buch vor" style="left:65px;top:370px;width:230px;height:230px;background:linear-gradient(135deg,#f0e6e2,#b8a69a 50%,#5e6f80)"></div>
    <div class="badge" style="left:27px;top:362px;width:92px;height:92px">Hier bekommen Sie das passende Pflegepaket maßgeschneidert</div>
  </div>
</section>

</body>
</html>
```